Seminar Workbook Template

My first project is a Workbook Template. There is a sample attached to give you an idea of the layout I like. I have added notes, in blue, to show what I want. I do want a header that will brand the workbook (should have the logo). We are looking for someone that we can continue to work 1 -1 with other, collateral projects. We want a constant look and feel and we have two projects ready to go.

Target Market(s)

My clients are Office Managers and CPAs so I want the workbook to have a professional layout and match the look and feel of my website: LedgerVineworks.com

Requirements
Must have
• Must match the feel of the Website. Must be in Word .doc format.
Should not have
• No red.

```html
<!DOCTYPE html>
<html lang="en">
<head>
<meta charset="utf-8">
<title>Seminar Workbook Template – Ledger Vineworks</title>
<link rel="stylesheet" href="https://fonts.googleapis.com/css2?family=Raleway:wght@600;700;800&family=Lato:wght@400;700&display=swap">
<style>
  :root{
    --backdrop:#b4b4b4;
    --paper:#ffffff;
    --ink:#111111;
    --body:#555555;
    --rule:#8a8a8a;
    --green:#2ebd85;
    --green-deep:#13965e;
    --green-light:#3cc891;
    --quote:#4a4a4a;
  }
  html,body{margin:0;padding:0;width:1200px;height:859px;overflow:hidden;background:var(--backdrop);}
  .stage{position:absolute;left:0;top:0;width:1500px;height:1074px;transform:scale(.8);transform-origin:0 0;background:var(--backdrop);}
  .page-label{position:absolute;top:40px;width:660px;text-align:center;font:700 30px/1 "Raleway",sans-serif;color:var(--ink);letter-spacing:.5px;}
  .page{position:absolute;top:99px;width:660px;height:934px;background:var(--paper);box-shadow:0 2px 6px rgba(0,0,0,.35);overflow:hidden;}
  .page-one{left:57px}
  .page-two{left:777px}
  .page-shapes{position:absolute;left:0;top:0;width:660px;height:934px;}
  .footer-note{position:absolute;left:0;right:0;top:903px;text-align:center;white-space:nowrap;color:#fff;font:700 12.5px/1 "Lato",sans-serif;letter-spacing:.4px;}

  .brand-seal{position:absolute;left:25px;top:18px;width:160px;height:160px;border-radius:50%;background:#fff;border:3px solid #2b2b2b;box-shadow:inset 0 0 0 6px #fff,inset 0 0 0 8px #8a8a8a;display:flex;align-items:center;justify-content:center;text-align:center;}
  .brand-name{font:800 21px/1.15 "Raleway",sans-serif;color:#1e6b45;letter-spacing:1px;text-transform:uppercase;}

  .lesson-title{position:absolute;right:18px;top:20px;text-align:right;color:#fff;font-family:"Raleway",sans-serif;}
  .lesson-title .module{font-weight:800;font-size:25px;letter-spacing:.5px;}
  .lesson-title .module .bar{font-weight:400;margin:0 6px}
  .lesson-title .topic{font-weight:600;font-size:19px;letter-spacing:.8px;margin-top:4px}

  .section-bar{position:absolute;height:34px;background:linear-gradient(90deg,var(--green-deep),var(--green-light));color:#fff;font:700 16px/34px "Raleway",sans-serif;text-align:center;letter-spacing:.2px;white-space:nowrap;}
  .ribbon{position:absolute;height:35px;color:#fff;font:700 16px/35px "Raleway",sans-serif;padding-left:15px;box-sizing:border-box;background:linear-gradient(90deg,var(--green-deep),var(--green-light));clip-path:polygon(0 0,100% 0,92% 50%,100% 100%,0 100%);white-space:nowrap;}

  .intro-box{position:absolute;left:28px;top:213px;width:273px;height:364px;box-sizing:border-box;border:1.5px dashed #777;border-radius:14px;padding:18px 14px 0 16px;font:400 13px/19px "Lato",sans-serif;color:var(--body);}
  .intro-box p{margin:0 0 18px}

  .check{position:absolute;width:16px;height:16px;border:2.5px solid var(--green);border-radius:50%;background:radial-gradient(circle at 40% 35%,#fff 55%,#e6f7ef 100%);}
  .task{position:absolute;left:411px;font:400 13px/1 "Lato",sans-serif;color:var(--body);white-space:nowrap;}
  .rule{position:absolute;height:0;border-top:1.3px dashed var(--rule);}

  .body-copy{position:absolute;font:400 13px/19px "Lato",sans-serif;color:var(--body);}

  .quote-card{position:absolute;left:370px;top:102px;width:253px;height:251px;box-sizing:border-box;border:1.5px dashed var(--green);border-radius:10px;overflow:hidden;}
  .quote-card .section-bar{position:static;border-radius:8px 8px 0 0;height:35px;line-height:35px}
  .quote-mark{display:block;margin:14px auto 0;width:46px;height:38px}
  .quote-text{margin:6px 8px 0;text-align:center;font:400 15px/19px "Lato",sans-serif;color:var(--body);}
</style>
</head>
<body>
<div class="stage">
  <div class="page-label" style="left:57px">PAGE 01</div>
  <div class="page-label" style="left:777px">PAGE 02</div>

  <section class="page page-one">
    <svg class="page-shapes" viewBox="0 0 660 934" aria-hidden="true">
      <path d="M0 0H660V76C540 96 400 104 270 92C160 82 70 66 0 84Z" fill="var(--green)"/>
      <path d="M0 84C70 66 160 82 270 92C400 104 540 96 660 76V92C540 112 400 114 270 104C170 96 80 92 0 112Z" fill="var(--ink)"/>
      <path d="M0 830C18 866 60 886 140 886H660V934H0Z" fill="var(--ink)"/>
    </svg>

    <div class="brand-seal"><span class="brand-name">Ledger<br>Vineworks</span></div>

    <div class="lesson-title">
      <div class="module">MODULE 1<span class="bar">|</span>LESSON 3</div>
      <div class="topic">RESEARCH YOUR AUDIENCE</div>
    </div>

    <div class="intro-box">
      <p>Lorem Ipsum is simply dummy text of the printing and typesetting industry.</p>
      <p>Lorem Ipsum has been the industry's standard dummy text ever since the 1500s, when an unknown printer took a galley of type and scrambled.</p>
      <p>It to make a type specimen book. It has survived not only five centuries, but also the leap into electronic.</p>
      <p>Remaining essentially unchanged. It was popularised in the 1960s. More recently with desktop publishing software like Inkwell Layout including versions of Lorem Ipsum.</p>
    </div>

    <div class="section-bar" style="left:370px;top:140px;width:253px">TO BE DONE</div>
    <span class="check" style="left:377px;top:190px"></span><span class="task" style="top:194px">Lorem Ipsum is simply dummy text.</span>
    <span class="check" style="left:377px;top:225px"></span><span class="task" style="top:229px">Lorem Ipsum is simply dummy text.</span>
    <span class="check" style="left:377px;top:261px"></span><span class="task" style="top:265px">Lorem Ipsum is simply dummy text.</span>
    <span class="check" style="left:377px;top:296px"></span><span class="task" style="top:300px">Lorem Ipsum is simply dummy text.</span>
    <span class="check" style="left:377px;top:332px"></span><span class="task" style="top:336px">Lorem Ipsum is simply dummy text.</span>
    <span class="check" style="left:377px;top:367px"></span><span class="task" style="top:371px">Lorem Ipsum is simply dummy text.</span>

    <div class="section-bar" style="left:370px;top:429px;width:253px">ETC...</div>
    <span class="check" style="left:377px;top:481px"></span><span class="rule" style="left:411px;top:499px;width:212px"></span>
    <span class="check" style="left:377px;top:510px"></span><span class="rule" style="left:411px;top:528px;width:212px"></span>
    <span class="check" style="left:377px;top:539px"></span><span class="rule" style="left:411px;top:557px;width:212px"></span>
    <span class="check" style="left:377px;top:568px"></span><span class="rule" style="left:411px;top:586px;width:212px"></span>

    <div class="section-bar" style="left:370px;top:634px;width:253px">STUCK | STALLED | NEED HELP</div>
    <span class="rule" style="left:377px;top:704px;width:246px"></span>
    <span class="rule" style="left:377px;top:733px;width:246px"></span>
    <span class="rule" style="left:377px;top:762px;width:246px"></span>
    <span class="rule" style="left:377px;top:791px;width:246px"></span>
    <span class="rule" style="left:377px;top:820px;width:246px"></span>
    <span class="rule" style="left:377px;top:850px;width:246px"></span>

    <div class="ribbon" style="left:0;top:622px;width:201px">3 LISTENING POSTS</div>
    <span class="check" style="left:16px;top:681px"></span>
    <span class="check" style="left:16px;top:739px"></span>
    <span class="check" style="left:16px;top:797px"></span>
    <span class="rule" style="left:56px;top:704px;width:245px"></span>
    <span class="rule" style="left:56px;top:733px;width:245px"></span>
    <span class="rule" style="left:56px;top:762px;width:245px"></span>
    <span class="rule" style="left:56px;top:791px;width:245px"></span>
    <span class="rule" style="left:56px;top:820px;width:245px"></span>
    <span class="rule" style="left:56px;top:850px;width:245px"></span>

    <div class="footer-note">Copyright © 2018 Dana Holt | LessonCraftStudio.com eCourse Blueprint. All rights reserved.</div>
  </section>

  <section class="page page-two">
    <svg class="page-shapes" viewBox="0 0 660 934" aria-hidden="true">
      <path d="M0 0H660V28C560 48 420 40 270 18C170 4 70 12 0 36Z" fill="var(--green)"/>
      <path d="M0 36C70 12 170 4 270 18C420 40 560 48 660 28V44C560 64 420 56 270 32C160 18 60 34 0 60Z" fill="var(--ink)"/>
      <path d="M0 800C10 850 50 884 140 886H660V934H0Z" fill="var(--ink)"/>
    </svg>

    <div class="section-bar" style="left:28px;top:63px;width:267px">AH-HAS AND WINS</div>
    <span class="rule" style="left:40px;top:132px;width:243px"></span>
    <span class="rule" style="left:40px;top:161px;width:243px"></span>
    <span class="rule" style="left:40px;top:191px;width:243px"></span>
    <span class="rule" style="left:40px;top:220px;width:243px"></span>

    <div class="section-bar" style="left:28px;top:264px;width:267px">HOW LONG SHOULD THIS TAKE?</div>
    <p class="body-copy" style="left:32px;top:312px;width:250px;margin:0">Lorem Ipsum is simply dummy text of the printing and typesetting industry. Lorem Ipsum has been the industry's standard dummy text ever since the 1500s.</p>

    <div class="quote-card">
      <div class="section-bar">MOTIVATIONAL QUOTE</div>
      <svg class="quote-mark" viewBox="0 0 46 38" aria-hidden="true">
        <path d="M2 38V22C2 10 8 3 19 0l2 5C14 8 11 12 11 18h9v20Z M25 38V22C25 10 31 3 42 0l2 5C37 8 34 12 34 18h9v20Z" fill="var(--quote)"/>
      </svg>
      <p class="quote-text">Lorem Ipsum is simply dummy text of the printing and typesetting industry. Lorem Ipsum has been the industry's standard dummy text ever since the 1500s, when an unknown printer took.</p>
    </div>

    <div class="section-bar" style="left:196px;top:430px;width:268px">IDEAS AND NOTES</div>
    <span class="rule" style="left:32px;top:507px;width:597px"></span>
    <span class="rule" style="left:32px;top:538px;width:597px"></span>
    <span class="rule" style="left:32px;top:569px;width:597px"></span>
    <span class="rule" style="left:32px;top:600px;width:597px"></span>
    <span class="rule" style="left:32px;top:631px;width:597px"></span>
    <span class="rule" style="left:32px;top:663px;width:597px"></span>
    <span class="rule" style="left:32px;top:694px;width:597px"></span>
    <span class="rule" style="left:32px;top:725px;width:597px"></span>
    <span class="rule" style="left:32px;top:757px;width:597px"></span>
    <span class="rule" style="left:32px;top:788px;width:597px"></span>
    <span class="rule" style="left:32px;top:819px;width:597px"></span>
    <span class="rule" style="left:32px;top:850px;width:597px"></span>

    <div class="footer-note">Copyright © 2018 Dana Holt | LessonCraftStudio.com eCourse Blueprint. All rights reserved.</div>
  </section>
</div>
</body>
</html>
```